Heronfield Wealth Advisors, Inc. Marketing Collateral - 401k Rollover Decisions

We are looking to create a branded one-pager marketing collateral piece talking about 401k Rollovers & the important information people should know. Rough draft of concept & content included below, and we will finalize copy later. Would include a call to action to contact us. Our website and other contact information are available at https://growwithmaplecrest.com/.

Target Market(s)

Working adults ages 55-75 with access to retirement accounts or who have a 401k account. Especially interested in appealing to people who work for small businesses, local businesses, have company stock, and other unique needs in this space.

Industry/Entity Type

Financial services

Font styles to use
Other font styles liked:
• Cambria

Requirements
Must have
• Clear message & call to action
Nice to have
• Highlight how many Americans have been changing jobs since COVID and why it would be worth working with a professional to make decisions on what to do with retirement accounts and assets. (We're working on getting that stat)
Should not have
• Too much text, don't want to inundate with text blocks

```html
<!DOCTYPE html>
<html lang="en">
<head>
<meta charset="utf-8">
<title>Heronfield Wealth Advisors – 401(k) Rollover Decisions</title>
<link rel="stylesheet" href="https://fonts.googleapis.com/css2?family=Caladea:wght@400;700&family=Open+Sans:wght@400;600&display=swap">
<style>
  :root {
    --red: #c8102e;
    --red-deep: #b20d27;
    --ink: #1d1d1f;
    --white: #ffffff;
    --paper: #f5f5f6;
    --rule: #d9d9dc;
    --stage: #0d3148;
    --serif: "Caladea", Cambria, Georgia, serif;
    --sans: "Open Sans", Arial, sans-serif;
  }
  * { box-sizing: border-box; margin: 0; padding: 0; }
  html, body { width: 1200px; height: 2168px; overflow: hidden; }
  body { background: var(--stage); position: relative; font-family: var(--serif); color: var(--ink); }

  .flyer {
    position: absolute; left: 30px; top: 278px;
    width: 1140px; height: 1613px;
    background: linear-gradient(180deg, var(--white) 0%, var(--paper) 60%, var(--white) 100%);
    overflow: hidden;
    box-shadow: 0 18px 40px rgba(0,0,0,.35);
  }
  .abs { position: absolute; }

  .photo-couple {
    left: 556px; top: 201px; width: 584px; height: 381px;
    background: linear-gradient(135deg, #d9cfc4 0%, #b9aa99 45%, #8f8479 100%);
  }
  .header-shape { left: 0; top: 0; width: 1140px; height: 560px; }

  .brand { left: 74px; top: 78px; display: flex; align-items: center; gap: 22px; color: var(--ink); font-family: var(--serif); font-weight: 400; }
  .brand-mark { width: 72px; height: 72px; background: var(--red); flex: none; }
  .brand-name { font-size: 54px; line-height: 1; letter-spacing: 1px; }
  .brand-sub { display: block; font-size: 17px; letter-spacing: 2.6px; margin-top: 6px; text-transform: uppercase; }

  .contact { left: 651px; top: 58px; }
  .contact-label { color: var(--red); font-size: 44px; line-height: 1.1; }
  .contact-phone { display: flex; align-items: center; gap: 22px; font-size: 60px; line-height: 1.1; color: var(--ink); margin-top: 4px; }
  .contact-phone svg { width: 38px; height: 38px; }

  .headline {
    left: 68px; top: 232px; width: 620px;
    color: var(--white); font-size: 35px; line-height: 47px; font-weight: 400;
  }

  .options { left: 0; top: 582px; width: 1140px; height: 228px; background: rgba(255,255,255,.92); }
  .option { position: absolute; top: 0; width: 280px; margin-left: -140px; text-align: center; }
  .option-icon {
    width: 124px; height: 124px; margin: 0 auto; border-radius: 50%;
    background: var(--ink); border: 6px solid #e7e7e9; display: flex; align-items: center; justify-content: center;
    margin-top: -14px;
  }
  .option-icon svg { width: 66px; height: 66px; }
  .option-label { color: var(--red); font-size: 56px; font-weight: 700; margin-top: 34px; line-height: 1; }
  .divider { position: absolute; top: 12px; width: 4px; height: 200px; background: linear-gradient(180deg, var(--red) 0%, var(--red) 55%, var(--ink) 100%); }

  .photo-meeting {
    left: 16px; top: 811px; width: 553px; height: 364px;
    background: linear-gradient(120deg, #d8d8da 0%, #b8b4b0 40%, #6f6a6a 100%);
  }
  .advice {
    left: 569px; top: 834px; width: 571px; height: 316px;
    background: var(--red); color: var(--white);
    font-family: var(--sans); font-size: 20px; line-height: 31px;
    padding: 46px 30px 0 36px;
  }

  .compare-title { left: 0; top: 1180px; width: 1140px; text-align: center; color: var(--red); font-size: 34px; }
  .compare {
    left: 70px; top: 1248px; width: 995px; height: 268px;
    border: 4px solid var(--ink); border-top: 6px solid var(--red); border-bottom: none;
    background: var(--white); display: flex;
  }
  .compare-col { flex: 1; padding: 0 18px; }
  .compare-col + .compare-col { border-left: 4px solid var(--ink); }
  .compare-head { color: var(--red); font-size: 38px; line-height: 54px; border-bottom: 1px solid var(--rule); padding-left: 0; }
  .compare-list { list-style: none; }
  .compare-list li {
    position: relative; padding: 10px 0 10px 68px; min-height: 70px;
    font-size: 18px; line-height: 24px; border-bottom: 1px solid var(--rule);
  }
  .compare-list li:last-child { border-bottom: none; }
  .tick { position: absolute; left: 14px; top: 10px; width: 24px; height: 24px; }

  .footer {
    left: 0; top: 1513px; width: 1140px; height: 100px; background: var(--red);
    color: var(--white); text-align: center; font-size: 42px; line-height: 100px;
  }
</style>
</head>
<body>
<main class="flyer">
  <div class="abs photo-couple" role="img" aria-label="Photo of a smiling older couple sharing a blanket outdoors"></div>

  <svg class="abs header-shape" viewBox="0 0 1140 560" aria-hidden="true">
    <path fill="var(--red)" d="M548 0 L578 0 C598 0 610 14 618 34 L655 150 C665 180 665 200 655 230 L560 510 C552 530 540 541 515 541 L0 541 L0 200 L510 200 C560 200 590 175 575 130 L548 0 Z"/>
  </svg>

  <div class="abs brand">
    <span class="brand-mark"></span>
    <div>
      <span class="brand-name">HERONFIELD</span>
      <span class="brand-sub">Wealth Advisors, Inc.</span>
    </div>
  </div>

  <div class="abs contact">
    <div class="contact-label">Call Us:</div>
    <div class="contact-phone">
      <svg viewBox="0 0 24 24"><path fill="var(--red)" d="M6.6 10.8a15.1 15.1 0 0 0 6.6 6.6l2.2-2.2a1 1 0 0 1 1-.25 11.4 11.4 0 0 0 3.6.57 1 1 0 0 1 1 1V20a1 1 0 0 1-1 1A17 17 0 0 1 3 4a1 1 0 0 1 1-1h3.5a1 1 0 0 1 1 1c0 1.25.2 2.45.57 3.57a1 1 0 0 1-.25 1z"/></svg>
      <span>919-555-0148</span>
    </div>
  </div>

  <p class="abs headline">The most important thing to<br>realize when leaving an employer<br>is that you have options for the<br>money that you have worked<br>hard for and saved.</p>

  <section class="abs options">
    <div class="option" style="left:172px">
      <div class="option-icon"><svg viewBox="0 0 64 64"><circle cx="34" cy="20" r="13" fill="#fff"/><text x="34" y="26" text-anchor="middle" font-size="17" font-family="Arial" font-weight="700" fill="#1d1d1f">$</text><path fill="#fff" d="M6 40h10l10 4h12a3 3 0 0 1 0 6H26v2h14l14-8a3 3 0 0 1 4 4L42 58H6z"/></svg></div>
      <div class="option-label">Leave it</div>
    </div>
    <span class="divider" style="left:312px"></span>
    <div class="option" style="left:445px">
      <div class="option-icon"><svg viewBox="0 0 64 64"><path fill="#fff" d="M34 8h12l-4 8h-4zM30 20h20c8 8 10 16 10 24 0 9-6 14-20 14s-20-5-20-14c0-8 2-16 10-24z"/><text x="40" y="48" text-anchor="middle" font-size="18" font-family="Arial" font-weight="700" fill="#1d1d1f">$</text><ellipse cx="14" cy="50" rx="10" ry="4" fill="#fff"/><ellipse cx="14" cy="42" rx="10" ry="4" fill="#fff"/><ellipse cx="14" cy="34" rx="10" ry="4" fill="#fff"/></svg></div>
      <div class="option-label">Roll it</div>
    </div>
    <span class="divider" style="left:573px"></span>
    <div class="option" style="left:720px">
      <div class="option-icon"><svg viewBox="0 0 64 64"><path fill="#fff" d="M4 26 18 12l14 14h-4v10H8V26zM32 44l14-14 14 14h-4v12H36V44z"/><path fill="none" stroke="#fff" stroke-width="4" d="M36 12c10 0 16 4 18 12M28 54c-10 0-16-4-18-12"/><path fill="#fff" d="M50 24h10l-5 6zM14 42H4l5-6z"/></svg></div>
      <div class="option-label">Move it</div>
    </div>
    <span class="divider" style="left:862px"></span>
    <div class="option" style="left:1001px">
      <div class="option-icon"><svg viewBox="0 0 64 64"><circle cx="34" cy="22" r="15" fill="none" stroke="#fff" stroke-width="4"/><text x="34" y="29" text-anchor="middle" font-size="20" font-family="Arial" font-weight="700" fill="#fff">$</text><path fill="#fff" d="M4 42h10l10 4h12a3 3 0 0 1 0 6H24v2h14l16-9a3 3 0 0 1 4 4L40 60H4z"/></svg></div>
      <div class="option-label">Take it</div>
    </div>
  </section>

  <div class="abs photo-meeting" role="img" aria-label="Photo of an older woman in conversation with a younger advisor at a desk"></div>

  <p class="abs advice">We recommend working with an expert who has experience with a multitude of different types of qualified plans such as 401(k), 403(b), Employee Stock Ownership Plans, SEP IRAs, etc. Not all plan types are eligible for rollovers, and even if they are, they may vary in the types of plans that they can be rolled in to.</p>

  <h2 class="abs compare-title" style="font-weight:400">Rolling over 401(k) assets to IRA</h2>

  <section class="abs compare">
    <div class="compare-col">
      <h3 class="compare-head" style="font-weight:400">Pros</h3>
      <ul class="compare-list">
        <li><svg class="tick" viewBox="0 0 24 24"><circle cx="12" cy="12" r="12" fill="var(--red)"/><path d="M6.5 12.5l3.5 3.5 7-7.5" fill="none" stroke="#fff" stroke-width="2.6"/></svg>Typically more investment choices in an IRA</li>
        <li><svg class="tick" viewBox="0 0 24 24"><circle cx="12" cy="12" r="12" fill="var(--red)"/><path d="M6.5 12.5l3.5 3.5 7-7.5" fill="none" stroke="#fff" stroke-width="2.6"/></svg>Ability to make contributions to the account<br>even after leaving your former employer</li>
        <li><svg class="tick" viewBox="0 0 24 24"><circle cx="12" cy="12" r="12" fill="var(--red)"/><path d="M6.5 12.5l3.5 3.5 7-7.5" fill="none" stroke="#fff" stroke-width="2.6"/></svg>Choice of investment custodian and investment<br>advisor you work with</li>
      </ul>
    </div>
    <div class="compare-col">
      <h3 class="compare-head" style="font-weight:400">Cons</h3>
      <ul class="compare-list">
        <li><svg class="tick" viewBox="0 0 24 24"><circle cx="12" cy="12" r="12" fill="var(--red)"/><path d="M6.5 12.5l3.5 3.5 7-7.5" fill="none" stroke="#fff" stroke-width="2.6"/></svg>Less protection from creditors</li>
        <li><svg class="tick" viewBox="0 0 24 24"><circle cx="12" cy="12" r="12" fill="var(--red)"/><path d="M6.5 12.5l3.5 3.5 7-7.5" fill="none" stroke="#fff" stroke-width="2.6"/></svg>Less access to funds prior to age 59½</li>
        <li><svg class="tick" viewBox="0 0 24 24"><circle cx="12" cy="12" r="12" fill="var(--red)"/><path d="M6.5 12.5l3.5 3.5 7-7.5" fill="none" stroke="#fff" stroke-width="2.6"/></svg>RMDs on funds at age 72<br>regardless if you are still working</li>
      </ul>
    </div>
  </section>

  <footer class="abs footer">www.growwithmaplecrest.com</footer>
</main>
</body>
</html>
```